Harbor Allied BC

I have a baseline business card that I would like to spruce up!

I actually like this business card. I just want to find a way to have all the information below on it and it too look balanced and professional.

Target Market(s)

Small to medium sized companies - Health Insurance Consulting

Industry/Entity Type

Health Insurance

Contact Information for Business Card

The information I would like included on the business card is:

- Harbor Allied Southridge Title and logo
- Tessa Wrenfield
- Business title: Principal
- 4192 Cobalt Ridge Rd Suite D-117 Fernhollow, WA 98999
- Employee Benefits Consulting & (Wellness Consulting) optional
- tessa@harboralliedsr.example
- cell: 425-555-0183

Font styles to use
Other font styles liked:
• I like the font it is currently in but am open to others.

Requirements
Must have
• I like the logo and the color scheme. I even like the layout. I just need to fine tune it!

```html
<!DOCTYPE html>
<html lang="en">
<head>
<meta charset="utf-8">
<title>Harbor Allied Southridge — Business Card</title>
<link rel="stylesheet" href="https://fonts.googleapis.com/css2?family=Lato:ital,wght@0,300;0,400;0,700;1,300&display=swap">
<style>
  :root {
    --brand-green: #008351;
    --ink: #1e1e1e;
    --ink-soft: #444444;
    --paper: #ffffff;
    --stage: #ececec;
    --rule: #9a9a9a;
  }
  * { box-sizing: border-box; margin: 0; padding: 0; }
  html, body {
    width: 1200px; height: 586px; overflow: hidden;
    background: var(--stage);
    font-family: "Lato", Arial, sans-serif;
  }
  .canvas { position: relative; width: 1200px; height: 586px; }

  .card {
    position: absolute; top: 129px;
    width: 502px; height: 301px;
  }
  .card-front { left: 65px; background: var(--brand-green); }
  .card-back { left: 608px; background: var(--paper); }

  /* Front */
  .front-mark {
    position: absolute; left: 78px; top: 112px;
    width: 74px; height: 74px; border-radius: 50%;
    background: var(--ink);
  }
  .front-name {
    position: absolute; left: 166px; top: 118px;
    font-size: 25px; font-weight: 700; line-height: 1.1;
    letter-spacing: 0.5px; color: var(--ink); text-transform: uppercase;
  }

  /* Back */
  .back-mark {
    position: absolute; left: 88px; top: 42px;
    width: 54px; height: 54px; border-radius: 50%;
    background: var(--brand-green);
  }
  .back-name {
    position: absolute; left: 152px; top: 48px; width: 186px;
    text-align: right;
    font-size: 17px; font-weight: 700; line-height: 1.15;
    letter-spacing: 0.3px; color: var(--ink); text-transform: uppercase;
  }
  .divider {
    position: absolute; left: 351px; top: 37px;
    width: 1px; height: 70px; background: var(--rule);
  }
  .services {
    position: absolute; left: 362px; top: 52px;
    font-size: 11.5px; font-weight: 300; line-height: 1.2;
    color: var(--ink-soft);
  }

  .contact { position: absolute; left: 34px; top: 194px; }
  .contact-line {
    display: flex; align-items: center; gap: 7px;
    font-size: 12.5px; font-weight: 300; color: var(--ink-soft);
    height: 21px;
  }
  .contact-line svg { width: 12px; height: 12px; flex: none; }
  .address {
    margin-top: 6px;
    font-size: 12.5px; font-weight: 400; line-height: 1.38; color: var(--ink);
  }

  .person {
    position: absolute; right: 32px; top: 200px; text-align: right;
  }
  .person-name { font-size: 19px; font-weight: 400; color: var(--ink); }
  .person-name strong { font-weight: 700; }
  .person-title {
    font-size: 16px; font-weight: 300; font-style: italic;
    color: var(--ink-soft); margin-top: 1px;
  }

  .base-band {
    position: absolute; left: 0; bottom: 0;
    width: 100%; height: 10px; background: var(--brand-green);
  }
</style>
</head>
<body>
<main class="canvas">
  <section class="card card-front" aria-label="Card front">
    <span class="front-mark"></span>
    <div class="front-name">Harbor Allied<br>Southridge</div>
  </section>

  <section class="card card-back" aria-label="Card back">
    <span class="back-mark"></span>
    <div class="back-name">Harbor Allied<br>Southridge</div>
    <span class="divider"></span>
    <div class="services">Employee<br>Benefits<br>Consulting</div>

    <div class="contact">
      <div class="contact-line">
        <svg viewBox="0 0 12 12" aria-hidden="true">
          <path fill="var(--brand-green)" d="M1 4.2C1 2.6 3.3 2 6 2s5 .6 5 2.2V5H8.6V3.9H3.4V5H1z M3 5.6h6l1.5 4.9H1.5z"/>
          <circle cx="6" cy="7.8" r="1.3" fill="#fff"/>
        </svg>
        <span>425-555-0183</span>
      </div>
      <div class="contact-line">
        <svg viewBox="0 0 12 12" aria-hidden="true">
          <rect x="0.5" y="2.5" width="11" height="7.5" fill="var(--brand-green)"/>
          <path d="M1 3l5 4 5-4" fill="none" stroke="#fff" stroke-width="1"/>
        </svg>
        <span>tessa@harboralliedsr.example</span>
      </div>
      <p class="address">4192 Cobalt Ridge Rd Suite<br>D-117 Fernhollow, WA 98999</p>
    </div>

    <div class="person">
      <p class="person-name">Tessa <strong>Wrenfield</strong></p>
      <p class="person-title">Principal</p>
    </div>

    <span class="base-band"></span>
  </section>
</main>
</body>
</html>
```